Boat business cards

I'm looking for business cards with the two logos I've attached. I don't have an specific idea in mind and open to anything. All the usual info will be on the card. Name, position in company, nr, email, address, ect. The company rents out these two boats for charters and fishing.

```html
<!DOCTYPE html>
<html lang="en">
<head>
<meta charset="utf-8">
<title>Boat Charter Business Cards</title>
<link rel="stylesheet" href="https://fonts.googleapis.com/css2?family=Lato:wght@400;700&display=swap">
<style>
  :root{
    --bg:#1c1c1c;
    --card-white:#ffffff;
    --ink:#111111;
    --steel:#7196bf;
    --bright-blue:#5b86c9;
    --sand:#8a6c45;
    --mist:#c9c9c9;
    --graphite:#444444;
    --logo-grey:#5a5a5a;
  }
  *{margin:0;padding:0;box-sizing:border-box}
  html,body{width:1200px;height:1015px;overflow:hidden;background:var(--bg)}
  body{font-family:"Lato",sans-serif;display:flex;flex-direction:column;align-items:center;justify-content:center;gap:45px}
  .card{position:relative;width:770px;height:440px;background:var(--card-white);overflow:hidden}
  .card-art{position:absolute;inset:0;width:100%;height:100%}
  .brand{position:absolute;display:flex;flex-direction:column;align-items:center;gap:8px}
  .brand-art{border-radius:6px}
  .brand-name{font-weight:700;font-size:30px;letter-spacing:1px;color:var(--ink);white-space:nowrap}
  .brand-name.runner{color:var(--logo-grey)}
  .art-cruiser{width:250px;height:80px;background:linear-gradient(180deg,#e8e8e8 0%,#3a3a3a 45%,#9a7a52 70%,#cfdcef 100%)}
  .art-sportfish{width:260px;height:120px;background:linear-gradient(180deg,#e6e6e6 0%,#b8c4d4 40%,#8aa8d6 75%,#6b86b0 100%)}
  .website-back{position:absolute;left:40px;top:60px;color:#fff;font-size:22px;letter-spacing:1px}
  .holder{position:absolute;left:40px;bottom:40px;color:#fff}
  .holder-name{font-size:30px;font-weight:700;letter-spacing:.5px}
  .holder-role{font-size:22px;margin-top:2px}
  .contacts{position:absolute;right:36px;top:210px;color:#fff;font-size:20px;line-height:1.45;text-align:right;list-style:none}
  .contacts li{display:flex;justify-content:flex-end;align-items:center;gap:10px}
  .contacts svg{width:18px;height:18px;flex:none}
  .contacts .address{margin-top:10px;align-items:flex-start}
</style>
</head>
<body>

<section class="card card-back">
  <svg class="card-art" viewBox="0 0 770 440" preserveAspectRatio="none" aria-hidden="true">
    <path d="M0 0H770V40C600 45 520 80 430 190C340 300 200 330 0 345Z" fill="var(--bright-blue)" transform="translate(0,14)"/>
    <path d="M0 0H770V40C600 45 520 80 430 190C340 300 200 330 0 345Z" fill="var(--graphite)" transform="translate(0,7)"/>
    <path d="M0 0H770V40C600 45 520 80 430 190C340 300 200 330 0 345Z" fill="var(--ink)"/>
  </svg>
  <p class="website-back">www.websitename.com</p>
  <div class="brand" style="left:90px;top:300px">
    <div class="brand-art art-cruiser" role="img" aria-label="Illustration of a motor yacht"></div>
    <span class="brand-name">Polar Tide</span>
  </div>
  <div class="brand" style="left:470px;top:160px">
    <div class="brand-art art-sportfish" role="img" aria-label="Illustration of a sport fishing boat"></div>
    <span class="brand-name runner">Shore Runner</span>
  </div>
</section>

<section class="card card-front">
  <svg class="card-art" viewBox="0 0 770 440" preserveAspectRatio="none" aria-hidden="true">
    <path d="M0 440V300C200 300 320 280 410 180C490 90 600 50 770 40V440Z" fill="var(--mist)" transform="translate(0,-18)"/>
    <path d="M0 440V300C200 300 320 280 410 180C490 90 600 50 770 40V440Z" fill="var(--card-white)" transform="translate(0,-9)"/>
    <path d="M0 440V300C200 300 320 280 410 180C490 90 600 50 770 40V440Z" fill="var(--sand)" transform="translate(0,-4)"/>
    <path d="M0 440V300C200 300 320 280 410 180C490 90 600 50 770 40V440Z" fill="var(--steel)" transform="translate(0,6)"/>
  </svg>
  <div class="brand" style="left:50px;top:40px">
    <div class="brand-art art-sportfish" role="img" aria-label="Illustration of a sport fishing boat"></div>
    <span class="brand-name runner">Shore Runner</span>
  </div>
  <div class="brand" style="left:470px;top:16px">
    <div class="brand-art art-cruiser" role="img" aria-label="Illustration of a motor yacht"></div>
    <span class="brand-name">Polar Tide</span>
  </div>
  <div class="holder">
    <p class="holder-name">JONATHAN SMITH</p>
    <p class="holder-role">Managing Director</p>
  </div>
  <ul class="contacts">
    <li>044-123 456 789
      <svg viewBox="0 0 24 24"><path d="M6.6 10.8a15 15 0 006.6 6.6l2.2-2.2c.3-.3.7-.4 1-.2 1.1.4 2.3.6 3.6.6.6 0 1 .4 1 1V20c0 .6-.4 1-1 1A17 17 0 013 4c0-.6.4-1 1-1h3.5c.6 0 1 .4 1 1 0 1.3.2 2.5.6 3.6.1.3 0 .7-.2 1z" fill="#fff"/></svg></li>
    <li>info@webname.com
      <svg viewBox="0 0 24 24"><rect x="2" y="5" width="20" height="14" rx="1" fill="#fff"/><path d="M2 6l10 7 10-7" fill="none" stroke="var(--steel)" stroke-width="1.6"/></svg></li>
    <li>www.websitename.com
      <svg viewBox="0 0 24 24"><circle cx="12" cy="12" r="9" fill="none" stroke="#fff" stroke-width="2"/><path d="M3 12h18M12 3c3 3 3 15 0 18M12 3c-3 3-3 15 0 18" fill="none" stroke="#fff" stroke-width="1.6"/></svg></li>
    <li class="address"><span>421, Address line here<br>Country Name, 45452</span>
      <svg viewBox="0 0 24 24"><path d="M12 2a7 7 0 00-7 7c0 5 7 13 7 13s7-8 7-13a7 7 0 00-7-7z" fill="#fff"/><circle cx="12" cy="9" r="2.5" fill="var(--steel)"/></svg></li>
  </ul>
</section>

</body>
</html>
```